MALT HIGHLANDS/STONEFERN DISTILLERY

DOUBLE SIDED BUSINESS CARD ONE SIDE FOR WWW.MALTHIGHLANDS-EXAMPLE.ORG AND ONE SIDE FOR STONEFERN DISTILLERY ARTWORK FOR WEBSITE IS ATTACHED

1)
GORDON PRYCE CEO
MALT HIGHLANDS
Office 1 Harbour Court
14 Ferrier Row
Glasgow
Scotland, G5 2KX
W:WWW.MALTHIGHLANDS-EXAMPLE.ORG
E:GORDON@MALTHIGHLANDS-EXAMPLE.ORG
T:+44 7491 305718

2)
GORDON PRYCE CEO
STONEFERN DISTILLERY
Building 148, Werfpark Zandhoven,
3e Brederolaan, Katwijk, 2219KP

W: WWW.stonefern-example.nl
E: GORDON@stonefern-example.nl
T:+44 7491 305718

1)
Marieke Dool DIRECTOR
MALT HIGHLANDS
Office 1 Harbour Court
14 Ferrier Row
Glasgow
Scotland, G5 2KX
W:WWW.MALTHIGHLANDS-EXAMPLE.ORG
E:Marieke@MALTHIGHLANDS-EXAMPLE.ORG
T:+31 6 58137704

2)
MARIEKE DOOL DIRECTOR
STONEFERN DISTILLERY

E: marieke@stonefern-example.nl
T:+31 6 58137704

```html
<!DOCTYPE html>
<html lang="en">
<head>
<meta charset="utf-8">
<title>Malt Highlands / Stonefern Distillery – Business Card</title>
<link href="https://fonts.googleapis.com/css2?family=Arimo:wght@400;700&display=swap" rel="stylesheet">
<style>
  :root {
    --backdrop: #1d1d1d;
    --gold: #c69c3a;
    --gold-light: #d8bb66;
    --gold-deep: #7a6230;
    --ink: #111111;
    --dark: #1e1b19;
    --grey: #5d5a58;
    --white: #ffffff;
  }
  * { margin: 0; padding: 0; box-sizing: border-box; }
  html, body { width: 1200px; height: 930px; overflow: hidden; background: var(--backdrop); }
  body { font-family: "Arimo", Arial, sans-serif; color: var(--white); position: relative; }

  .card {
    position: absolute;
    width: 640px; height: 365px;
    border-radius: 18px;
    overflow: hidden;
    box-shadow: 0 6px 16px rgba(0,0,0,.6);
  }
  .card--front { left: 280px; top: 74px; background: var(--white); }
  .card--back  { left: 280px; top: 490px; background: linear-gradient(115deg, var(--dark) 0%, var(--dark) 62%, var(--grey) 80%, #4a4745 100%); }
  .card svg.card-art { position: absolute; inset: 0; width: 100%; height: 100%; }

  .brand {
    position: absolute;
    font-weight: 700;
    letter-spacing: 1px;
    white-space: nowrap;
  }
  .card--front .brand { right: 48px; top: 150px; font-size: 25px; color: var(--gold); }
  .card--front .brand .mark { display: inline-block; width: 12px; height: 12px; border-radius: 50%; background: var(--gold); margin-right: 10px; vertical-align: 3px; }
  .card--back .brand { right: 34px; top: 70px; font-size: 22px; color: var(--white); }
  .card--back .brand .mark { display: inline-block; width: 12px; height: 12px; background: var(--white); margin-right: 10px; vertical-align: 2px; }

  .person { position: absolute; left: 32px; top: 198px; }
  .person__name { font-size: 20px; font-weight: 700; line-height: 1; }
  .person__role { font-size: 15px; margin-top: 3px; }

  .contacts { position: absolute; left: 32px; top: 268px; list-style: none; font-size: 15px; }
  .contacts li { height: 22.5px; display: flex; align-items: center; gap: 8px; }
  .contacts svg { width: 13px; height: 13px; flex: none; }

  .address { position: absolute; right: 34px; top: 268px; text-align: right; font-size: 15px; font-style: normal; line-height: 22.5px; }
</style>
</head>
<body>

<section class="card card--front">
  <svg class="card-art" viewBox="0 0 640 365" preserveAspectRatio="none">
    <defs>
      <linearGradient id="frontGold" x1="0" y1="0" x2="1" y2="0">
        <stop offset="0" stop-color="#c49a36"/>
        <stop offset=".55" stop-color="#c89e3c"/>
        <stop offset=".68" stop-color="#dcc27c"/>
        <stop offset="1" stop-color="#c9a447"/>
      </linearGradient>
    </defs>
    <path d="M0,190 C40,125 120,102 200,118 C300,140 420,232 520,247 C580,255 620,215 640,183 L640,365 L0,365 Z" fill="url(#frontGold)"/>
    <path d="M82,123 C200,95 310,140 420,200 C480,232 530,246 572,238 C525,252 470,240 418,214 C300,152 200,112 82,123 Z" fill="var(--ink)"/>
  </svg>

  <div class="brand"><span class="mark"></span>MALT HIGHLANDS</div>

  <div class="person">
    <p class="person__name">GORDON PRYCE</p>
    <p class="person__role">CEO</p>
  </div>

  <ul class="contacts">
    <li><svg viewBox="0 0 16 16"><path d="M4 1l3 3-2 2c1 2 3 4 5 5l2-2 3 3-2 3C7 15 1 9 1 3z" fill="#fff"/></svg>+44 7491 305718</li>
    <li><svg viewBox="0 0 16 16"><rect x="1" y="3" width="14" height="10" fill="#fff"/><path d="M1 3l7 6 7-6" fill="none" stroke="#c69c3a" stroke-width="1.3"/></svg>GORDON@MALTHIGHLANDS-EXAMPLE.ORG</li>
    <li><svg viewBox="0 0 16 16"><circle cx="8" cy="8" r="7" fill="#fff"/><path d="M5 4c2 1 1 3 3 3s1 3 0 5M10 3c1 1 3 2 3 4" fill="none" stroke="#c69c3a" stroke-width="1.3"/></svg>WWW.MALTHIGHLANDS-EXAMPLE.ORG</li>
  </ul>

  <address class="address">
    Office 1 Harbour Court<br>
    14 Ferrier Row, Glasgow<br>
    Scotland, G5 2KX
  </address>
</section>

<section class="card card--back">
  <svg class="card-art" viewBox="0 0 640 365" preserveAspectRatio="none">
    <defs>
      <linearGradient id="backGold" x1="0" y1="0" x2="1" y2="1">
        <stop offset="0" stop-color="#d4b764"/>
        <stop offset=".45" stop-color="#a98d4c"/>
        <stop offset=".6" stop-color="#d9c48a"/>
        <stop offset="1" stop-color="#8a7240"/>
      </linearGradient>
      <linearGradient id="backShade" x1="0" y1="0" x2="0" y2="1">
        <stop offset="0" stop-color="#000" stop-opacity="0"/>
        <stop offset="1" stop-color="#000" stop-opacity=".35"/>
      </linearGradient>
    </defs>
    <path d="M0,194 C40,128 120,105 200,120 C300,140 420,232 520,247 C580,255 620,215 640,183 L640,365 L0,365 Z" fill="url(#backGold)"/>
    <path d="M0,194 C40,128 120,105 200,120 C300,140 420,232 520,247 C580,255 620,215 640,183 L640,365 L0,365 Z" fill="url(#backShade)"/>
    <path d="M84,126 C200,98 310,140 420,200 C480,232 530,246 572,238 C525,252 470,240 418,214 C300,154 200,114 84,126 Z" fill="var(--white)"/>
  </svg>

  <div class="brand"><span class="mark"></span>STONEFERN DISTILLERY</div>

  <div class="person" style="top:206px">
    <p class="person__name">GORDON PRYCE</p>
    <p class="person__role">CEO</p>
  </div>

  <ul class="contacts" style="top:278px">
    <li><svg viewBox="0 0 16 16"><path d="M4 1l3 3-2 2c1 2 3 4 5 5l2-2 3 3-2 3C7 15 1 9 1 3z" fill="#fff"/></svg>+44 7491 305718</li>
    <li><svg viewBox="0 0 16 16"><rect x="1" y="3" width="14" height="10" fill="#fff"/><path d="M1 3l7 6 7-6" fill="none" stroke="#a98d4c" stroke-width="1.3"/></svg>GORDON@stonefern-example.nl</li>
    <li><svg viewBox="0 0 16 16"><circle cx="8" cy="8" r="7" fill="#fff"/><path d="M5 4c2 1 1 3 3 3s1 3 0 5M10 3c1 1 3 2 3 4" fill="none" stroke="#a98d4c" stroke-width="1.3"/></svg>WWW.stonefern-example.nl</li>
  </ul>

  <address class="address" style="top:278px">
    Building 148<br>
    Werfpark Zandhoven,<br>
    3e Brederolaan, Katwijk, 2219KP
  </address>
</section>

</body>
</html>
```